Pull up banner design for mortgage broking firm $500 competition

Need a pull up banner design the banner will be
1.8m banner tall
Colours should be similar to our Logo blues and yellows
The logo at the top
the cloud house needs to be in the middle
the $500 needs to be big and stand out
The terms and conditions should be in dot points
the top line to be bigger than the bottom and different colour font.
Please see the attached dot point design down the bottom - but use yellow and blue colours.
the licensee details need to be in small print down the bottom.

```html
<!DOCTYPE html>
<html lang="en">
<head>
<meta charset="utf-8">
<title>Payforward Home Loans – $500 Health Check Banner</title>
<link href="https://fonts.googleapis.com/css2?family=Anton&family=Archivo+Black&family=Arimo:wght@400;700&family=Kalam:wght@700&display=swap" rel="stylesheet">
<style>
  :root{
    --sky-top:#1d86c9;
    --sky-mid:#3f9fdc;
    --sky-low:#a9d6f0;
    --panel-top:#3f76a6;
    --panel-bottom:#1b4a78;
    --footer:#173a5e;
    --box:#1690d6;
    --box-line:#bfe3f7;
    --yellow:#ffd21f;
    --yellow-deep:#f5a800;
    --navy:#123a63;
    --white:#ffffff;
    --logo-blue:#1c5ea8;
    --logo-orange:#f0a31c;
  }
  *{margin:0;padding:0;box-sizing:border-box}
  html,body{width:1200px;height:2699px;overflow:hidden;background:var(--white)}
  .banner{
    position:relative;width:1200px;height:2699px;overflow:hidden;
    background:linear-gradient(180deg,var(--sky-top) 0%,var(--sky-mid) 30%,var(--sky-low) 50%,var(--sky-low) 54%,var(--panel-top) 56%,var(--panel-bottom) 94%);
    font-family:"Arimo",Arial,sans-serif;
  }
  .brand{
    position:absolute;left:283px;top:27px;width:635px;height:239px;
    background:rgba(220,240,250,.92);border-radius:28px;
    display:flex;flex-direction:column;align-items:center;justify-content:center;gap:6px;
  }
  .brand-row{display:flex;align-items:center;gap:22px}
  .brand-dot{width:92px;height:92px;border-radius:50%;background:var(--logo-blue)}
  .brand-name{font-family:"Arimo",sans-serif;font-weight:700;font-size:62px;line-height:1.05;color:var(--logo-blue);text-align:left}
  .brand-tag{font-family:"Arimo",sans-serif;font-weight:700;font-size:34px;color:var(--logo-orange)}
  .headline{
    position:absolute;left:0;width:1200px;text-align:center;
    font-family:"Anton",Impact,sans-serif;color:var(--yellow);
    -webkit-text-stroke:3px #b86d00;
    text-shadow:0 6px 8px rgba(10,40,80,.45);
    line-height:1;
  }
  .h-savings{top:290px;font-size:142px;letter-spacing:1px}
  .h-or{top:436px;font-size:112px}
  .h-give{top:542px;font-size:130px}
  .h-amount{top:670px;font-size:268px;color:#fff23a;-webkit-text-stroke:4px #b86d00}
  .cash{position:absolute;border-radius:40px;opacity:.85;
    background:radial-gradient(ellipse at center,#c9d4b4 0%,#a7b58f 45%,rgba(160,180,140,0) 75%)}
  .cash-left{left:36px;top:639px;width:315px;height:495px}
  .cash-right{left:846px;top:639px;width:333px;height:495px}
  .cloud-house{position:absolute;left:360px;top:936px;width:486px;height:360px;border-radius:50%;
    background:radial-gradient(ellipse at center,#ffffff 0%,#e8f4fb 45%,rgba(200,230,248,0) 72%)}
  .offer{
    position:absolute;left:0;width:1200px;text-align:center;
    font-family:"Archivo Black",sans-serif;font-size:54px;line-height:1;color:var(--navy);
    -webkit-text-stroke:1.5px var(--white);
    text-shadow:0 0 6px #fff,0 0 2px #fff;
  }
  .offer-1{top:1337px}
  .offer-2{top:1411px}
  .terms{list-style:none}
  .term{position:absolute;left:50px;width:1125px}
  .tick{
    position:absolute;left:0;top:0;bottom:0;width:130px;
    background:var(--box);border:2px solid var(--box-line);
    display:flex;align-items:center;justify-content:center;
  }
  .term-body{
    position:absolute;left:152px;right:0;top:0;bottom:0;
    background:var(--box);border:2px solid var(--box-line);
    padding:14px 16px 0 16px;
  }
  .term-title{font-weight:700;font-size:28px;line-height:1.1;color:var(--yellow);text-transform:uppercase}
  .term-text{font-size:23px;line-height:1.3;color:var(--white);margin-top:4px}
  .footer{position:absolute;left:0;top:2565px;width:1200px;height:134px;background:var(--footer);
    padding:26px 36px 0;font-weight:700;font-size:20px;line-height:1.4;color:var(--yellow);text-transform:uppercase}
</style>
</head>
<body>
<div class="banner">
  <div class="brand">
    <div class="brand-row">
      <span class="brand-dot"></span>
      <span class="brand-name">PAYFORWARD<br>HOME LOANS</span>
    </div>
    <span class="brand-tag">paying it forward to you</span>
  </div>

  <div class="headline h-savings">WE GIVE YOU SAVINGS</div>
  <div class="headline h-or">OR</div>
  <div class="headline h-give">WE GIVE YOU</div>
  <div class="headline h-amount">$500</div>

  <div class="cash cash-left" role="img" aria-label="Banknotes flying out from a stack of cash"></div>
  <div class="cash cash-right" role="img" aria-label="Banknotes flying out from a stack of cash"></div>
  <div class="cloud-house" role="img" aria-label="A house shape formed by white clouds in a blue sky"></div>

  <div class="offer offer-1">FREE HOME LOAN HEALTH CHECK</div>
  <div class="offer offer-2">WITH A PFHL LENDING ADVISER!</div>

  <ul class="terms">
    <li class="term" style="top:1535px;height:114px">
      <span class="tick"><svg width="60" height="68" viewBox="0 0 60 68"><path d="M6 38 L22 60 L54 6" fill="none" stroke="#fff" stroke-width="7" stroke-linecap="round" stroke-linejoin="round"/></svg></span>
      <div class="term-body"><p class="term-title">Our Pay Forward policy is where the savings start</p><p class="term-text">All calculations of savings include PFHL Pay Forward policy of 0.15% on the running balance of your loan.</p></div>
    </li>
    <li class="term" style="top:1674px;height:113px">
      <span class="tick"><svg width="60" height="68" viewBox="0 0 60 68"><path d="M6 38 L22 60 L54 6" fill="none" stroke="#fff" stroke-width="7" stroke-linecap="round" stroke-linejoin="round"/></svg></span>
      <div class="term-body"><p class="term-title">At least $300,000 loan</p><p class="term-text">Your current loan size needs to be a minimum of $300,000.</p></div>
    </li>
    <li class="term" style="top:1814px;height:116px">
      <span class="tick"><svg width="60" height="68" viewBox="0 0 60 68"><path d="M6 38 L22 60 L54 6" fill="none" stroke="#fff" stroke-width="7" stroke-linecap="round" stroke-linejoin="round"/></svg></span>
      <div class="term-body"><p class="term-title">Must be local and in person</p><p class="term-text">Your appointment must be within 35km of Melbourne CBD and face-to-face with a PFHL adviser.</p></div>
    </li>
    <li class="term" style="top:1960px;height:115px">
      <span class="tick"><svg width="60" height="68" viewBox="0 0 60 68"><path d="M6 38 L22 60 L54 6" fill="none" stroke="#fff" stroke-width="7" stroke-linecap="round" stroke-linejoin="round"/></svg></span>
      <div class="term-body"><p class="term-title">The client must currently reside there</p><p class="term-text">Your current loan must be for the home you currently reside in.</p></div>
    </li>
    <li class="term" style="top:2099px;height:119px">
      <span class="tick"><svg width="60" height="68" viewBox="0 0 60 68"><path d="M6 38 L22 60 L54 6" fill="none" stroke="#fff" stroke-width="7" stroke-linecap="round" stroke-linejoin="round"/></svg></span>
      <div class="term-body" style="padding-top:8px"><p class="term-title">Must be with big 4 home loans only Harbour, Summit, Coastal or Meridian branded home loans</p><p class="term-text">Must be a big four loan easily accessible by the public.</p></div>
    </li>
    <li class="term" style="top:2243px;height:147px">
      <span class="tick"><svg width="60" height="68" viewBox="0 0 60 68"><path d="M6 38 L22 60 L54 6" fill="none" stroke="#fff" stroke-width="7" stroke-linecap="round" stroke-linejoin="round"/></svg></span>
      <div class="term-body"><p class="term-title">Must be an owner occupied loan with a variable rate and principal interest repayments</p><p class="term-text">All three of the above criteria must be met (PFHL specifically exclude investment loans, fixed interest and interest only loans.</p></div>
    </li>
    <li class="term" style="top:2419px;height:112px">
      <span class="tick"><svg width="60" height="68" viewBox="0 0 60 68"><path d="M6 38 L22 60 L54 6" fill="none" stroke="#fff" stroke-width="7" stroke-linecap="round" stroke-linejoin="round"/></svg></span>
      <div class="term-body"><p class="term-title">The loan must be at least 30 months old</p><p class="term-text">Must be at least 30 months since day of settlement.</p></div>
    </li>
  </ul>

  <footer class="footer">Clear Horizon Lending Pty Ltd trading as Payforward Home Loans ABN 12 345 678 901, authorised representative of Southern Finance Alliance ABN 98 765 432 109, Australian Credit License 123 456.</footer>
</div>
</body>
</html>
```